Swiss Injection Molding Company needs a 4-page Flyer

Velmar Plastik is a injection molding company based in Zurich, Switzerland. We are looking for a new 4-page Flyer to present our company, our services and our USPs to potential customers.

For more information, see the Briefing in the uploads

Font styles to use
Sans Serif

Colors
F0912C
F2A743
F7CA91
FBE8D2
FDF5EE

```html
<!DOCTYPE html>
<html lang="en">
<head>
<meta charset="utf-8">
<title>Velmar Plastik – Flyer</title>
<link href="https://fonts.googleapis.com/css2?family=Open+Sans:wght@400;600;700;800&display=swap" rel="stylesheet">
<style>
:root{
  --orange:#F07F22;
  --orange-light:#F2A743;
  --peach:#F7CA91;
  --cream:#FBE8D2;
  --dark:#4A4A4D;
  --ink:#333336;
  --panel:#F3F3F3;
  --stage:#EEEEEE;
  --white:#FFFFFF;
}
*{margin:0;padding:0;box-sizing:border-box}
html,body{width:1200px;height:459px;overflow:hidden;background:var(--stage);font-family:"Open Sans",Arial,sans-serif;color:var(--ink)}
.spread{position:absolute;top:43px;height:385px;background:var(--white);box-shadow:0 1px 4px rgba(0,0,0,.18);overflow:hidden}
.spread--outer{left:44px;width:539px}
.spread--inner{left:618px;width:540px}
.shapes{position:absolute;inset:0}
.abs{position:absolute}
.heading{font-weight:800;letter-spacing:.2px}
.tagline{left:31px;top:16px;width:210px;text-align:center;color:var(--white);font-size:10.5px}
.pill{position:absolute;height:14px;border-radius:7px;font-weight:800;font-size:8.5px;line-height:14px;text-align:center}
.pill--dark{background:var(--dark);color:var(--orange)}
.pill--orange{background:var(--orange);color:var(--white)}
.stat{left:12px;width:70px;text-align:center}
.stat__num{color:var(--orange);font-weight:800;font-size:22px;line-height:22px}
.stat__label{font-size:7px;line-height:8px;color:var(--ink);margin-top:1px}
.dots{left:18px;width:58px;top:150px;border-top:1px dotted var(--orange)}
.check{left:12px;width:70px;height:24px;border:1px solid #DDD;background:var(--white);font-size:6.2px;line-height:7.5px;padding:4px 0 0 20px;color:var(--ink)}
.check svg{position:absolute;left:3px;top:3px}
.benefits{left:96px;top:60px;width:167px;height:270px;background:var(--panel)}
.benefit{left:108px;width:160px}
.benefit__icon{position:absolute;left:0;top:0;width:24px;height:24px;border-radius:50%}
.benefit__title{position:absolute;left:28px;top:-4px;font-weight:600;font-size:7px;white-space:nowrap}
.benefit__text{position:absolute;left:28px;top:7px;font-size:7px;line-height:9px;color:#555}
.reference{left:123px;top:257px;width:117px;height:42px;border:1px solid #DDD;background:var(--white);border-radius:3px}
.reference__tag{left:35px;top:-6px;width:50px;height:11px;line-height:11px;font-size:6px;border-radius:6px}
.reference__names{position:absolute;left:6px;right:6px;top:14px;display:grid;grid-template-columns:1fr 1fr;row-gap:4px;font-weight:700;font-size:7px;color:var(--ink);text-align:center}
.footer-text{left:60px;top:340px;font-size:7.2px;line-height:8.4px;color:var(--white)}
.footer-square{left:176px;top:338px;width:25px;height:25px;background:var(--white)}
.footer-mail{left:176px;top:365px;font-size:7.2px;color:var(--white)}
.brand{left:280px;top:15px;width:250px;text-align:center;color:var(--white);font-weight:700;font-size:22px;letter-spacing:1.5px;line-height:26px}
.brand-sub{left:280px;top:49px;width:250px;text-align:center;color:var(--orange);font-size:11px}
.photo-round{left:306px;top:93px;width:192px;height:192px;border-radius:50%;z-index:1;background:radial-gradient(circle at 45% 40%,#F6F6F6 0%,#E2E2E2 45%,#F4A260 75%,#E8782A 100%)}
.photo-ring{left:299px;top:86px;width:206px;height:206px;border-radius:50%;border:3px solid var(--orange)}
.partner-banner{left:340px;top:279px;width:124px;height:19px;z-index:2;background:var(--orange);clip-path:polygon(0 0,100% 0,95% 100%,5% 100%);color:var(--white);font-size:9.5px;line-height:19px;text-align:center;white-space:nowrap}
.partner-line{left:300px;top:302px;width:200px;text-align:center;color:var(--orange);font-size:10.5px;line-height:14px;white-space:nowrap}
.partner-line span{display:inline-block;padding-bottom:1px;border-bottom:1px solid var(--orange)}
.cover-list{left:287px;top:333px;list-style:none;font-size:7px;line-height:10px;color:#555}
.cover-list li::before{content:"•";color:var(--orange);margin-right:3px}
.seal{top:348px;width:21px;height:21px;border-radius:50%}
.section-title{color:var(--white);text-align:center}
.card{left:38px;width:220px;background:var(--white);box-shadow:0 1px 3px rgba(0,0,0,.2)}
.card--dark{background:var(--dark)}
.card__title{position:absolute;left:19px;top:4px;color:var(--orange);font-weight:800;font-size:9.5px}
.card__body{position:absolute;left:19px;top:18px;width:140px;font-size:6.2px;line-height:7.5px;color:var(--ink);text-align:justify}
.card--dark .card__body{width:194px;color:var(--white)}
.card__body p+p{margin-top:2px}
.card__photo{position:absolute;right:4px;top:3px;width:54px;bottom:3px;background:linear-gradient(135deg,#D9DEE3,#8E969E)}
.step-badge{left:11px;width:46px;height:46px;border-radius:50%;background:var(--orange)}
.step-badge svg{position:absolute;left:8px;top:8px}
.tech{border:1px solid var(--orange);background:var(--white)}
.tech__head{position:absolute;left:6px;right:6px;top:3px;height:30px;font-weight:800;font-size:7px;line-height:8.5px;text-align:center;padding-top:7px}
.tech__head--orange{background:var(--orange);color:var(--white)}
.tech__head--dark{background:var(--dark);color:var(--orange)}
.tech__list{position:absolute;left:6px;right:4px;top:38px;list-style:none;font-size:6.2px;line-height:7.5px;color:var(--ink)}
.tech__list li{padding-left:6px;text-indent:-5px}
.tech__list li::before{content:"• "}
.tech__photo{width:46px;height:46px;border-radius:50%;border:2px solid var(--orange)}
</style>
</head>
<body>

<section class="spread spread--outer">
  <svg class="shapes" width="539" height="385" viewBox="0 0 539 385" aria-hidden="true">
    <defs>
      <linearGradient id="pellet" x1="0" y1="0" x2="1" y2="1">
        <stop offset="0" stop-color="#F39A3E"/><stop offset="1" stop-color="#E9731C"/>
      </linearGradient>
    </defs>
    <path d="M0 0H269V62Q160 112 0 82Z" fill="url(#pellet)"/>
    <path d="M0 335Q140 305 269 342V385H0Z" fill="var(--orange)"/>
    <path d="M0 344Q140 312 269 350V385H0Z" fill="var(--dark)"/>
    <path d="M269 0H539V70Q410 150 269 60Z" fill="var(--dark)"/>
    <path d="M269 60Q410 150 539 70V78Q410 155 269 66Z" fill="var(--orange)"/>
  </svg>

  <div class="abs heading tagline">SWISS INJECTION MOLDING EXPERTS</div>

  <div class="pill pill--dark" style="left:12px;top:84px;width:70px">ABOUT US</div>
  <div class="abs stat" style="top:112px"><div class="stat__num">30</div><div class="stat__label">EMPLOYEES</div></div>
  <div class="abs dots"></div>
  <div class="abs stat" style="top:158px"><div class="stat__num">25</div><div class="stat__label">INJECTION<br>MOLDING MACHINES</div></div>

  <div class="abs check" style="top:215px"><svg width="12" height="12" viewBox="0 0 12 12"><circle cx="6" cy="6" r="6" fill="var(--orange)"/><path d="M3 6.2 5.1 8.2 9 4" stroke="#fff" stroke-width="1.5" fill="none"/></svg>IN-HOUSE<br>TOOLMAKING</div>
  <div class="abs check" style="top:246px"><svg width="12" height="12" viewBox="0 0 12 12"><circle cx="6" cy="6" r="6" fill="var(--orange)"/><path d="M3 6.2 5.1 8.2 9 4" stroke="#fff" stroke-width="1.5" fill="none"/></svg>ISO 9001<br>CERTIFIED</div>
  <div class="abs check" style="top:277px"><svg width="12" height="12" viewBox="0 0 12 12"><circle cx="6" cy="6" r="6" fill="var(--orange)"/><path d="M3 6.2 5.1 8.2 9 4" stroke="#fff" stroke-width="1.5" fill="none"/></svg>FORMER ZTH<br>STARTUP</div>

  <div class="abs benefits"></div>
  <div class="pill pill--orange" style="left:123px;top:83px;width:117px">YOUR BENEFITS</div>

  <div class="abs benefit" style="top:116px">
    <div class="benefit__icon" style="background:var(--orange)"><svg width="24" height="24" viewBox="0 0 24 24"><circle cx="12" cy="12" r="6" fill="none" stroke="#fff" stroke-width="1.6"/><circle cx="12" cy="12" r="2" fill="#fff"/></svg></div>
    <div class="benefit__title">QUALITY «MADE IN SWITZERLAND»</div>
    <div class="benefit__text">Highest Precision thanks to<br>Swiss production</div>
  </div>
  <div class="abs benefit" style="top:161px">
    <div class="benefit__icon" style="background:var(--dark)"><svg width="24" height="24" viewBox="0 0 24 24"><rect x="6" y="9" width="9" height="7" fill="none" stroke="#fff" stroke-width="1.4"/><path d="M15 11h3l2 3v2h-5" fill="none" stroke="#fff" stroke-width="1.4"/><circle cx="9" cy="17" r="1.5" fill="#fff"/><circle cx="17" cy="17" r="1.5" fill="#fff"/></svg></div>
    <div class="benefit__title">FASTEST DELIVERY TIMES</div>
    <div class="benefit__text">Shorter time-to-market<br>and more iteration options</div>
  </div>
  <div class="abs benefit" style="top:206px">
    <div class="benefit__icon" style="background:var(--orange)"><svg width="24" height="24" viewBox="0 0 24 24"><path d="M6 10h12l-1-3H7Z" fill="none" stroke="#fff" stroke-width="1.4"/><rect x="7" y="10" width="10" height="7" fill="none" stroke="#fff" stroke-width="1.4"/><rect x="10.5" y="13" width="3" height="4" fill="#fff"/></svg></div>
    <div class="benefit__title">ONE-STOP-SHOP</div>
    <div class="benefit__text">Seamless partner from the first<br>prototype to series production</div>
  </div>

  <div class="abs reference">
    <div class="pill pill--orange reference__tag">REFERENCE</div>
    <div class="reference__names"><span>ALVENA</span><span>kerntor</span><span>MEDARO</span><span>sonilis</span></div>
  </div>

  <div class="abs footer-text">
    <svg width="6" height="8" viewBox="0 0 6 8" style="position:absolute;left:-8px;top:10px"><path d="M3 8 0.6 4A2.6 2.6 0 1 1 5.4 4Z" fill="#fff"/><circle cx="3" cy="2.8" r="1" fill="var(--dark)"/></svg>
    <svg width="7" height="7" viewBox="0 0 7 7" style="position:absolute;left:-8px;top:26px"><path d="M1 0.5 2.5 0.5 3 2.3 2 3A4 4 0 0 0 4 5L4.7 4 6.5 4.5V6A5.5 5.5 0 0 1 1 0.5Z" fill="#fff"/></svg>
    Velmar Plastik AG<br>Lindenweg 12, 8005 Zurich<br>Switzerland<br>+41 44 000 12 34
  </div>
  <div class="abs footer-square"></div>
  <div class="abs footer-mail">info@velmarplastik.ch</div>

  <div class="abs brand">VELMAR PLASTIK</div>
  <div class="abs heading brand-sub">SWISS INJECTION MOLDING EXPERTS</div>

  <div class="abs photo-ring"></div>
  <div class="abs photo-round" role="img" aria-label="Photo of injection molded parts, connectors, circuit boards and orange plastic pellets"></div>

  <div class="abs heading partner-banner">YOUR PARTNER FOR</div>
  <div class="abs heading partner-line"><span>COMPLEX PLASTIC SOLUTIONS</span></div>
  <ul class="abs cover-list">
    <li>Injection molded prototypes within a few days</li>
    <li>(Micro) injection molding with in-house toolmaking</li>
    <li>Overmolding and custom solutions</li>
    <li>Connectors and cable assemblies</li>
  </ul>
  <div class="abs seal" style="left:474px;border:1.5px solid #AAA;background:#F2F2F2"></div>
  <div class="abs seal" style="left:498px;border:1.5px solid var(--orange);background:#E1251B"></div>
</section>

<section class="spread spread--inner">
  <svg class="shapes" width="540" height="385" viewBox="0 0 540 385" aria-hidden="true">
    <path d="M0 0H270V8Q135 -6 0 18Z" fill="var(--dark)"/>
    <path d="M0 0H270V10Q135 70 0 10Z" fill="var(--orange)"/>
    <path d="M0 10Q135 70 270 10V14Q135 80 0 18Z" fill="var(--dark)"/>
    <path d="M270 0H540V18Q405 80 270 12Z" fill="var(--dark)"/>
    <path d="M270 12Q405 80 540 18V26Q405 88 270 18Z" fill="var(--orange)"/>
    <path d="M56 22H100M166 22H210" stroke="#fff" stroke-width=".8"/>
    <path d="M325 20H358M452 20H485" stroke="#fff" stroke-width=".8"/>
  </svg>

  <div class="abs heading section-title" style="left:70px;top:12px;width:126px;font-size:15px">SERVICE</div>
  <div class="abs heading section-title" style="left:340px;top:8px;width:130px;font-size:11px;line-height:13px">TECHNOLOGY<br>RANGE</div>

  <div class="abs step-badge" style="top:63px"><svg width="30" height="30" viewBox="0 0 30 30"><path d="M15 1 27 8V22L15 29 3 22V8Z" fill="#fff"/><circle cx="15" cy="13" r="4.5" fill="none" stroke="var(--orange)" stroke-width="1.3"/><path d="M13 18h4M13.5 20h3" stroke="var(--orange)" stroke-width="1.2"/></svg></div>
  <div class="abs card" style="top:50px;height:72px">
    <div class="card__title">IDEA</div>
    <div class="card__body"><p><b>Engineering &amp; design</b> – We support you from the initial idea onwards with our many years of experience in design and optimization</p><p><b>Material selection</b> – With over 600 materials in stock and expertise from 1,000 applications, we help you select the right plastic</p></div>
    <div class="card__photo" role="img" aria-label="Photo of an engineer presenting a 3D part design on a screen"></div>
  </div>

  <div class="abs step-badge" style="top:143px"><svg width="30" height="30" viewBox="0 0 30 30"><path d="M15 1 27 8V22L15 29 3 22V8Z" fill="#fff"/><circle cx="14" cy="14" r="5" fill="none" stroke="var(--orange)" stroke-width="1.4"/><path d="M17.5 17.5 21 21" stroke="var(--orange)" stroke-width="1.6"/></svg></div>
  <div class="abs card" style="top:129px;height:73px">
    <div class="card__title">EVALUATION</div>
    <div class="card__body"><p><b>Prototyping</b> – Using a rapid tooling process developed at ZTH Zurich, we can implement your ideas in near-series production within a very short time</p><p><b>Iterations</b> – Variants &amp; design ideas can be tested quickly &amp; easily until the optimal solution is found</p></div>
    <div class="card__photo" role="img" aria-label="Photo of a designer working on a CAD model at a monitor"></div>
  </div>

  <div class="abs step-badge" style="top:222px"><svg width="30" height="30" viewBox="0 0 30 30"><path d="M15 1 27 8V22L15 29 3 22V8Z" fill="#fff"/><path d="M15 8 21 11.5V18.5L15 22 9 18.5V11.5ZM9 11.5 15 15 21 11.5M15 15V22" fill="none" stroke="var(--orange)" stroke-width="1.2"/></svg></div>
  <div class="abs card" style="top:209px;height:72px">
    <div class="card__title">PRE-SERIES</div>
    <div class="card__body"><p><b>Toolmaking</b> – Thanks to our in-house tool-making facility, high-precision components can be produced &amp; tested in the shortest possible time</p><p><b>3D printing</b> – For prototypes or small series, we use additive processes as a flexible supplement to injection molding</p></div>
    <div class="card__photo" role="img" aria-label="Photo of a technician at a precision measuring machine"></div>
  </div>

  <div class="abs step-badge" style="top:306px"><svg width="30" height="30" viewBox="0 0 30 30"><path d="M15 1 27 8V22L15 29 3 22V8Z" fill="#fff"/><circle cx="15" cy="15" r="5.5" fill="none" stroke="var(--orange)" stroke-width="1.3" stroke-dasharray="2.2 1.2"/><circle cx="15" cy="15" r="2.5" fill="none" stroke="var(--orange)" stroke-width="1.2"/></svg></div>
  <div class="abs card card--dark" style="top:286px;height:86px">
    <div class="card__title">PRODUCTION</div>
    <div class="card__body"><p><b>100% Made in Switzerland</b> – All our products are produced and tested entirely in-house in Zurich. With quality that is ISO 9001 certified</p><p><b>Broad industry support</b> – Thanks to our customers, we are familiar with the requirements of a wide range of industries. These include the mechanical and electrical engineering industries, the pharmaceutical industry, medical and laboratory technology, aviation, and many more</p></div>
  </div>

  <div class="abs tech" style="left:280px;top:92px;width:117px;height:119px">
    <div class="tech__head tech__head--orange">INJECTION MOLDED<br>PROTOTYPES</div>
    <ul class="tech__list">
      <li><b>Speed</b> – prototypes in the original material within a few days</li>
      <li><b>Material selection</b> – over 600 materials in stock: from PP to PEEK, from TPEs to silicone</li>
      <li><b>Flexibility</b> – we injection mold small series of 1–100 pieces on specially developed prototype machines</li>
    </ul>
  </div>
  <div class="abs tech__photo" style="left:317px;top:53px;background:radial-gradient(circle,#6FB06A,#3A3A3C 70%)" role="img" aria-label="Photo of colorful molded prototype parts"></div>

  <div class="abs tech" style="left:404px;top:92px;width:118px;height:119px">
    <div class="tech__head tech__head--dark">(MICRO) INJECTION<br>MOLDING</div>
    <ul class="tech__list">
      <li><b>Toolmaking</b> – We produce complex molds in-house, including slides, polished &amp; eroded surfaces</li>
      <li><b>Capacity</b> – We manufacture series of 100 to 1,000,000 pieces in our modern machine park</li>
      <li><b>Precision</b> – Tolerances in the hundredths range and component weights below 0.1 grams are part of our everyday business</li>
    </ul>
  </div>
  <div class="abs tech__photo" style="left:441px;top:52px;background:radial-gradient(circle,#6A6A6A,#202020 70%)" role="img" aria-label="Photo of a micro injection mold tool"></div>

  <div class="abs tech" style="left:281px;top:253px;width:117px;height:121px">
    <div class="tech__head tech__head--dark">OVERMOLDING AND<br>CUSTOM SOLUTIONS</div>
    <ul class="tech__list">
      <li><b>Material connections</b> – Overmolding of glass, ceramic, metal, or plastic parts</li>
      <li><b>Integration</b> – Reliable embedding of electronics, sensors, or LEDs directly into the injection molded part</li>
      <li><b>Protection &amp; function</b> – Special processes ensure stability, tightness, and long service life</li>
    </ul>
  </div>
  <div class="abs tech__photo" style="left:317px;top:215px;background:radial-gradient(circle,#E6E8EC,#9EA3AA 75%)" role="img" aria-label="Photo of overmolded glass lens parts"></div>

  <div class="abs tech" style="left:405px;top:253px;width:118px;height:121px">
    <div class="tech__head tech__head--orange">CONNECTORS AND<br>CABLE SOLUTIONS</div>
    <ul class="tech__list">
      <li><b>Customized</b> – development of individual connectors tailored to your requirements, even for small series</li>
      <li><b>Everything from a single source</b> – cable assembly &amp; overmolding completely in-house in Zurich</li>
      <li><b>Reliability</b> – robust, tight, and durable solutions for the most demanding environments</li>
    </ul>
  </div>
  <div class="abs tech__photo" style="left:442px;top:215px;background:radial-gradient(circle,#FFFFFF,#B8C4B0 80%)" role="img" aria-label="Photo of connector cable assemblies"></div>
</section>

</body>
</html>
```